BOLD & MINIMALIST DESIGN NEEDED

We want a very bold but minimalistic business card design that is impactful and utilizes both sides of the business card. Our current logo is included for your use.

We want bold fonts and good use of negative space. We don't want the logo to overpower the design.

Target Market(s)

Professionals who are building new commercial buildings.

Industry/Entity Type

Construction

Contact Information for Business Card

Name, Title, email, office phone, cell phone, website

Font styles to use
Serif
Sans Serif

Requirements
Must have
• Bold design!

```html
<!DOCTYPE html>
<html lang="en">
<head>
<meta charset="utf-8">
<title>Summitline Business Card</title>
<link rel="stylesheet" href="https://fonts.googleapis.com/css2?family=Roboto:wght@700;900&family=Roboto+Condensed:wght@700&display=swap">
<style>
  :root {
    --backdrop: #dfe4e2;
    --card: #ffffff;
    --ink: #111111;
    --text-grey: #555555;
    --accent: #7cc242;
    --card-edge: #1a1a1a;
  }
  * { margin: 0; padding: 0; box-sizing: border-box; }
  html, body {
    width: 1200px;
    height: 716px;
    overflow: hidden;
    background: var(--backdrop);
  }
  .canvas {
    position: relative;
    width: 1200px;
    height: 716px;
  }
  .card {
    position: absolute;
    left: 369px;
    width: 461px;
    height: 264px;
    background: var(--card);
    border-radius: 12px;
    box-shadow: -2px 2px 0 var(--card-edge);
    overflow: hidden;
  }
  .card--front { top: 94px; }
  .card--back { top: 382px; }

  .brand {
    position: absolute;
    display: flex;
    align-items: center;
    font-family: "Roboto", Arial, sans-serif;
    font-weight: 900;
    color: var(--ink);
    letter-spacing: 0.5px;
  }
  .brand__mark {
    background: var(--accent);
    flex: none;
  }
  .card--front .brand {
    left: 0; right: 0; top: 0; bottom: 0;
    justify-content: center;
    gap: 12px;
    font-size: 38px;
    padding-bottom: 24px;
  }
  .card--front .brand__mark { width: 30px; height: 30px; }

  .card--back .brand {
    left: 20px;
    top: 200px;
    gap: 7px;
    font-size: 20px;
  }
  .card--back .brand__mark { width: 16px; height: 16px; }

  .holder {
    position: absolute;
    right: 17px;
    top: 20px;
    text-align: right;
    font-family: "Roboto", Arial, sans-serif;
    font-weight: 700;
    color: var(--text-grey);
  }
  .holder__name { font-size: 16px; line-height: 20px; }
  .holder__title { font-size: 12px; line-height: 15px; margin-top: 2px; }

  .rule {
    position: absolute;
    left: 0;
    top: 50px;
    width: 382px;
    height: 2px;
    background: var(--ink);
  }

  .contact {
    position: absolute;
    right: 16px;
    top: 147px;
    text-align: right;
    font-family: "Roboto Condensed", Arial, sans-serif;
    font-weight: 700;
    font-size: 12.5px;
    line-height: 16.5px;
    color: var(--text-grey);
    list-style: none;
  }
  .contact__gap { margin-top: 14px; }
</style>
</head>
<body>
<main class="canvas">
  <section class="card card--front" aria-label="Card front">
    <div class="brand">
      <span class="brand__mark"></span>
      <span class="brand__name">SUMMITLINE</span>
    </div>
  </section>

  <section class="card card--back" aria-label="Card back">
    <div class="holder">
      <p class="holder__name">Dana Morrow</p>
      <p class="holder__title">Designer</p>
    </div>
    <div class="rule"></div>

    <div class="brand">
      <span class="brand__mark"></span>
      <span class="brand__name">SUMMITLINE</span>
    </div>

    <ul class="contact">
      <li>P : +123-45-67890</li>
      <li>E : info@youremail.com</li>
      <li>W : www.infoweibsite.com</li>
      <li class="contact__gap">A : Your Address Here</li>
      <li>R. No. 05 P.O. 5400, BD</li>
    </ul>
  </section>
</main>
</body>
</html>
```